Simple Lawyer Business Card Design Project with gold foil

Looking for a double sided business card. I would like to incorporate two of the images I attached onto the card- a monogram M in a circle and the legal image.
I also added image # 2 as a possibility of how to incorporate both images and for the layout of the information.

Back Side: This side of card will be one version in maroon and one version in white. The logo/vector on back side of card with business name Crandell Legal Group. Shield/Vector should be placed above the Crandell Legal Group lettering in a gold foil press. Please use colors of attachment #3.

Front Side: front of card will be white. front of card could have the monogram M in circle on background (where the lightened scales are on the sample card), with company information over it- Crandell Legal Group. *please delete the crown image above the M* Would like to see the monogram logo in gold -Crandell Legal Group will be in gold foil. Everything on left side should be black font.

Velda Orsini, Esq.
Principal Attorney
Address: 18 Harwick Ave. Suite 212 Woodcliff Lake,
NJ 07419
Phone: 201-739-5186
Fax: 201-826-3947
Email: vorsini@kestrolaw.example
www.kestrolaw.example

Industry/Entity Type

Lawyer

Contact Information for Business Card

Velda Orsini, Esq.
Principal Attorney
Address: 18 Harwick Ave. Suite 212 Woodcliff Lake, NJ 07419
Phone: 201-739-5186
Fax: 201-826-3947
www.kestrolaw.example

Font styles to use
Serif
Other font styles liked:
• fonts on samples

Colors
ffffff

Requirements
Must have
• - The final files must conform w/:
• - https://www.quillpress.example/silk-w-stamped-foil-business-cards
• - https://www.quillpress.example/template-files/business-cards/3.5x2.zip
• - https://www.vidstream.example/watch?v=Q2rTk7LpZxa#action=share
• - we would ask that you upload single page .pdf files only.
• - we recommend a Rich Black value of C=60, M=40, Y=40, K=100
• - Foil mask files are set up just like our Spot UV mask files. The file will only be black and white. The black areas will show where you want the foil placed. White will show areas where you do not want the foil. When ordering a Foil Stamp job with Spot UV, you must provide separate mask files for the Foil (foil mask) and Spot UV (spuv mask). Up to Six files would need to be provided.
• - When using Foil, please keep in mind that Foil and UV can not overlap and we recommend avoiding the use of small/fine text or fonts for foil objects. For best results, please be sure foil coverage is less than 50% of the artwork area.
• - It’s also important to note that there may be up to 1/16" shift on the placement of the foil. Keep this in mind if you are trying to align foil with other printed artwork.
Should not have
• don't want anything cluttered

```html
<!DOCTYPE html>
<html lang="en">
<head>
<meta charset="utf-8">
<title>Crandell Legal Group — Business Cards</title>
<link href="https://fonts.googleapis.com/css2?family=Source+Sans+3:wght@400;600;700&display=swap" rel="stylesheet">
<style>
  :root {
    --backdrop: #3b3531;
    --card-black: #0d0d0d;
    --card-edge: #1c1c1c;
    --gold: #d6a63c;
    --gold-light: #f1cf73;
    --silver: #c9c9c9;
    --ink-light: #e8e8e8;
    --muted-line: #8a6a24;
  }
  * { box-sizing: border-box; margin: 0; padding: 0; }
  html, body {
    width: 1200px; height: 900px; overflow: hidden;
    background: var(--backdrop);
    font-family: "Source Sans 3", "Helvetica Neue", Arial, sans-serif;
  }
  .canvas {
    position: relative; width: 1200px; height: 900px;
  }
  .card {
    position: absolute; top: 301px;
    width: 520px; height: 297px;
    background: var(--card-black);
    border: 1px solid var(--card-edge);
    box-shadow: 0 10px 24px rgba(0,0,0,.45);
  }
  .card--front { left: 50px; }
  .card--back { left: 630px; }

  /* front */
  .brand-mark {
    position: absolute; left: 26px; top: 48px;
    width: 190px; height: 200px;
    display: flex; flex-direction: column; align-items: center; justify-content: center; gap: 16px;
  }
  .brand-ring {
    width: 110px; height: 110px; border-radius: 50%;
    border: 5px solid var(--gold);
  }
  .brand-name {
    color: var(--gold); font-weight: 600; font-size: 17px;
    letter-spacing: .5px; text-align: center; line-height: 1.2;
  }
  .divider {
    position: absolute; left: 232px; top: 38px; width: 1px; height: 222px;
    background: linear-gradient(to bottom, transparent, var(--muted-line) 20%, var(--muted-line) 80%, transparent);
  }
  .contact {
    position: absolute; left: 252px; top: 44px; right: 16px;
    color: var(--ink-light);
  }
  .contact__name { color: var(--gold-light); font-weight: 700; font-size: 17px; line-height: 1.1; }
  .contact__title { font-size: 13px; margin-top: 2px; }
  .contact__address { font-size: 13px; line-height: 1.3; margin-top: 14px; }
  .contact__list { list-style: none; margin-top: 12px; font-size: 13px; line-height: 1.4; }
  .contact__list li { display: flex; align-items: center; gap: 8px; }
  .contact__list svg { width: 10px; height: 10px; flex: none; fill: var(--gold); }

  /* back */
  .firm-name {
    position: absolute; left: 0; right: 0; top: 118px;
    text-align: center; color: var(--silver);
    font-weight: 600; font-size: 34px; letter-spacing: 2px;
  }
</style>
</head>
<body>
<main class="canvas">
  <section class="card card--front" aria-label="Card front">
    <div class="brand-mark">
      <div class="brand-ring"></div>
      <div class="brand-name">Crandell Legal Group</div>
    </div>
    <div class="divider"></div>
    <div class="contact">
      <p class="contact__name">Velda Orsini, Esq.</p>
      <p class="contact__title">Attorney at Law</p>
      <p class="contact__address">18 Harwick Ave. Suite 212 Woodcliff<br>Lake, NJ 07419</p>
      <ul class="contact__list">
        <li><svg viewBox="0 0 10 10"><path d="M2 0h2l1 3-1.5 1a6 6 0 0 0 2.5 2.5L7 5l3 1v2a2 2 0 0 1-2 2A8 8 0 0 1 0 2a2 2 0 0 1 2-2z"/></svg>201-739-5186</li>
        <li><svg viewBox="0 0 10 10"><path d="M2 0h5v3H2zM0 4h10v5H0z"/></svg>201-826-3947</li>
        <li><svg viewBox="0 0 10 10"><path d="M0 2h10v6H0zM0 2l5 3.5L10 2" stroke="#0d0d0d" stroke-width=".8"/></svg>vorsini@kestrolaw.example</li>
        <li><svg viewBox="0 0 10 10"><circle cx="5" cy="5" r="5"/></svg>www.kestrolaw.example</li>
      </ul>
    </div>
  </section>

  <section class="card card--back" aria-label="Card back">
    <p class="firm-name">Crandell Legal Group</p>
  </section>
</main>
</body>
</html>
```